Long Established Local Fencing (not swords) Business needs fresh Business Cards

We need fresh double sided business cards for our Fencing Construction business, we are looking for something with our new logo design added, and maybe a photo background ?
We recently had cards made from Cardlyne and we were horrified with what we got back, the quality was terrible, so am looking for high quality format for good printing company to make.
We install Steelmora, Timber paling, Aluminium Slat Screening, Picket (timber and aluminium) and most other fencing installations.
Our website is brankelrails.com.au should you like to learn a bit more.
We do have logo in other formats if required.
We have been in business for over 35 years and we have used this as a "motto" it is on our signage

Industry/Entity Type

Construction

Contact Information for Business Card

Open to ideas, we need 3 x different cards, one generic with no name and 2 x others each with 1 of our bosses name on each, I will put into upload files.

Colors
ec1f27
000000
606060
f5f5f5

Requirements
Must have
• Company Name and Logo
• Address
• Contact details, phone, website, email etc
• Small space to write notes when leaving card at residence
Nice to have
• Our motto "Servicing the Peninsula for over 35 years"

```html
<!DOCTYPE html>
<html lang="en">
<head>
<meta charset="utf-8">
<title>Brankel Rails – Business Card</title>
<link href="https://fonts.googleapis.com/css2?family=Open+Sans:wght@400;600;700;800&display=swap" rel="stylesheet">
<style>
  :root {
    --red: #ec1f27;
    --black: #000000;
    --ink: #141414;
    --grey: #606060;
    --paper: #f5f5f5;
    --white: #ffffff;
    --stage: #e7e4df;
  }
  * { box-sizing: border-box; margin: 0; padding: 0; }
  html, body { width: 1200px; height: 1000px; overflow: hidden; }
  body {
    position: relative;
    background: var(--stage);
    font-family: "Open Sans", Arial, sans-serif;
  }
  .card {
    position: absolute;
    left: 266px;
    width: 666px;
    height: 397px;
    overflow: hidden;
    box-shadow: 0 6px 18px rgba(0,0,0,0.25);
  }
  .card--front {
    top: 74px;
    background: radial-gradient(ellipse at 40% 45%, #1e1e1e 0%, var(--ink) 70%);
  }
  .card--back {
    top: 533px;
    background: var(--white);
  }
  .wordmark {
    position: absolute;
    display: flex;
    align-items: center;
    gap: 16px;
    font-weight: 800;
    text-transform: uppercase;
    letter-spacing: 1px;
    white-space: nowrap;
  }
  .wordmark__square {
    display: block;
    background: var(--red);
  }
  .card--front .wordmark {
    left: 120px;
    top: 168px;
    font-size: 46px;
    color: var(--white);
  }
  .card--front .wordmark__square { width: 42px; height: 42px; }
  .card--back .wordmark {
    left: 34px;
    top: 72px;
    font-size: 40px;
    color: var(--ink);
  }
  .card--back .wordmark__square { width: 36px; height: 36px; }
  .swoosh {
    position: absolute;
    inset: 0;
  }
  .person {
    position: absolute;
    left: 33px;
    top: 192px;
  }
  .person__name {
    font-size: 19px;
    font-weight: 600;
    color: var(--ink);
    letter-spacing: 0.3px;
  }
  .person__role {
    font-size: 16px;
    color: var(--red);
    margin-top: 1px;
  }
  .contacts {
    position: absolute;
    left: 33px;
    top: 249px;
    list-style: none;
  }
  .contacts__item {
    display: flex;
    align-items: center;
    gap: 7px;
    font-size: 16px;
    color: var(--ink);
    line-height: 23px;
  }
  .icon { width: 14px; height: 14px; fill: var(--red); flex: none; }
  .address {
    position: absolute;
    right: 32px;
    top: 328px;
    text-align: right;
    font-size: 17px;
    line-height: 24px;
    color: var(--white);
    font-style: normal;
  }
  .address__line { display: flex; justify-content: flex-end; align-items: center; gap: 4px; }
</style>
</head>
<body>

  <section class="card card--front" aria-label="Card front">
    <div class="wordmark"><span class="wordmark__square"></span>Brankel Rails</div>
  </section>

  <section class="card card--back" aria-label="Card back">
    <svg class="swoosh" width="666" height="397" viewBox="0 0 666 397" aria-hidden="true">
      <path d="M0,347 C220,352 460,312 666,222 L666,397 L0,397 Z" fill="#141414"/>
      <path d="M120,344 C300,338 480,300 666,205 L666,214 C480,310 300,344 120,346 Z" fill="var(--red)"/>
      <path d="M0,340 C200,346 440,306 666,212 L666,222 C460,312 220,352 0,347 Z" fill="#ffffff"/>
    </svg>

    <div class="wordmark"><span class="wordmark__square"></span>Brankel Rails</div>

    <div class="person">
      <p class="person__name">DANIEL PRYCE</p>
      <p class="person__role">CEO / Owner</p>
    </div>

    <ul class="contacts">
      <li class="contacts__item">
        <svg class="icon" viewBox="0 0 24 24"><path d="M6.6 10.8a15.1 15.1 0 0 0 6.6 6.6l2.2-2.2a1 1 0 0 1 1-.25 11.4 11.4 0 0 0 3.6.57 1 1 0 0 1 1 1V20a1 1 0 0 1-1 1A17 17 0 0 1 3 4a1 1 0 0 1 1-1h3.5a1 1 0 0 1 1 1c0 1.250.2 2.450.57 3.57a1 1 0 0 1-.25 1z"/></svg>
        02 4187 5520
      </li>
      <li class="contacts__item">
        <svg class="icon" viewBox="0 0 24 24"><path d="M2 5h20v14H2z" fill="var(--red)"/><path d="M3.5 6.5l8.5 6.5 8.5-6.5" stroke="#fff" stroke-width="1.6" fill="none"/></svg>
        office@brankelrails.com.au
      </li>
      <li class="contacts__item">
        <svg class="icon" viewBox="0 0 24 24"><circle cx="12" cy="12" r="10"/><path d="M2 12h20M12 2c3 3 3 17 0 20M12 2c-3 3-3 17 0 20" stroke="#fff" stroke-width="1.5" fill="none"/></svg>
        www.brankelrails.com.au
      </li>
    </ul>

    <address class="address">
      <span class="address__line">
        <svg class="icon" viewBox="0 0 24 24"><path d="M12 2a7 7 0 0 0-7 7c0 5 7 13 7 13s7-8 7-13a7 7 0 0 0-7-7zm0 9.5A2.5 2.5 0 1 1 12 6.5a2.5 2.5 0 0 1 0 5z"/></svg>
        27 Harlow Avenue
      </span>
      <span class="address__line">Marlen Bay, Nsw 2391</span>
    </address>
  </section>

</body>
</html>
```